Webdesign fürs Mittagessen
Zielgruppe
Mit unserer Seite kann nach der nächsten Location suchen wo es was zu essen gibt. Das Angebot bezieht sich auf Food Trucks, Imbisse und Restaurants.
Kunden besuchen unsere Seite um dort anhand von Postleitzahlen/Städten nach Orten zu suchen wo es was zu Essen gibt.
Ebenso können Kunden mit guten Locations bei uns Stellplätze für Food Trucks anbieten.
Im angehängten Dokument sind 2 Screenshots der aktuellen Seite. Im Mittelpunkt der Seite steht die Suchfunktion. Das Design aus den Screenshots dient nicht als Orientierung, ebenso wenig wie das angehängt Logo!
Die angehängten Datei bitte ich vertraulich zu behandeln. Sie dürfen in keinster Weise weitergegeben werden oder veröffentlicht werden.
Aufgabenstellung
Das Design sollte übersichtlich und klar gestaltet sein.
Es sollte möglichst wenig knallige Farben haben.
Akzentfarben sind #E9A300 und #0A9DCD.

```html
<!DOCTYPE html>
<html lang="de">
<head>
<meta charset="utf-8">
<title>pausenteller – Mittagessen in deiner Nähe</title>
<link href="https://fonts.googleapis.com/css2?family=Open+Sans:ital,wght@0,400;0,600;0,700;1,600;1,700&display=swap" rel="stylesheet">
<style>
:root{
  --orange:#E9A300;
  --blue:#0A9DCD;
  --text:#555;
  --muted:#777;
  --line:#ddd;
  --field:#e6e6e6;
  --dark:#555;
  --white:#fff;
}
*{box-sizing:border-box;margin:0;padding:0}
html,body{width:1200px;height:821px;overflow:hidden}
body{font-family:"Open Sans",sans-serif;color:var(--text);position:relative;background:#d9c9b3}
.abs{position:absolute}
.topbar{left:0;top:0;width:1200px;height:48px;background:linear-gradient(90deg,#d8c7ae,#e6dac8 50%,#d3c1a7)}
.topbar .follow{left:249px;top:15px;font-size:10px;color:#fff;display:flex;align-items:center;gap:8px}
.topbar .follow i{width:8px;height:8px;border-radius:50%;background:#fff;display:inline-block}
.topbar .auth{left:889px;top:19px;font-size:11px;color:#fff}
.header{left:0;top:48px;width:1200px;height:182px;background:var(--white)}
.brand{left:232px;top:119px;font-size:21px;font-weight:700;color:var(--blue);display:flex;align-items:center;gap:8px}
.brand i{width:20px;height:20px;border-radius:50%;background:var(--blue);display:inline-block}
.tab{left:849px;top:77px;width:123px;height:26px;background:var(--blue);color:#fff;border-radius:5px 5px 0 0;font-size:11px;font-weight:700;padding:6px 0 0 11px;white-space:nowrap}
.search{left:414px;top:102px;width:564px;height:65px;background:var(--orange);padding:5px}
.search .inner{width:100%;height:100%;border:1px dashed #fff3c8;position:relative}
.field{position:absolute;top:9px;height:32px;background:#fff;font-size:11px;color:#666;padding:8px 7px;white-space:nowrap}
.drop{position:absolute;top:9px;height:32px;width:30px;background:var(--blue)}
.drop::after{content:"";position:absolute;left:9px;top:13px;border:6px solid transparent;border-top:7px solid #fff}
.go{position:absolute;left:469px;top:9px;width:80px;height:32px;background:var(--dark);color:#fff;font-size:11px;font-weight:700;text-align:center;line-height:32px}
.nav{left:211px;top:189px;width:778px;height:30px;border-top:1px solid var(--line);border-bottom:1px solid var(--line);font-size:14px;color:#666}
.nav span{display:flex;align-items:center;gap:7px;position:absolute;top:5px;white-space:nowrap}
.nav svg{width:20px;height:20px;fill:none;stroke:#888;stroke-width:1.3}
.photo{left:0;top:230px;width:1200px;height:591px;background:radial-gradient(ellipse at 30% 40%,#c79a73 0%,#b88c66 25%,#d8cab8 60%,#a9b28a 100%)}
.card{background:#fff;border-radius:5px}
h2{font-weight:400;font-size:16px;color:#555;display:flex;align-items:center;gap:9px;white-space:nowrap}
h2 em,.hl{color:var(--blue);font-style:italic;font-weight:700}
.welcome{left:215px;top:257px;width:473px;height:201px}
.welcome h2{position:absolute;left:28px;top:10px}
.welcome .lead{position:absolute;left:25px;top:41px;font-size:12.5px}
.welcome ul{position:absolute;left:28px;top:79px;list-style:none}
.welcome li{color:var(--orange);font-style:italic;font-weight:600;font-size:12px;height:22px;display:flex;align-items:center;gap:6px}
.welcome li i{width:16px;height:11px;border-radius:4px;background:#aaa;display:inline-block}
.welcome .voices{position:absolute;left:188px;top:68px;width:188px;height:83px;border-radius:8px;background:linear-gradient(135deg,#f2f2f2,#e4e4e4)}
.welcome .body{position:absolute;left:25px;top:157px;width:430px;font-size:9.5px;line-height:1.35;color:#555}
.news{left:701px;top:257px;width:280px;height:201px}
.news h2{position:absolute;left:21px;top:10px}
.news .mail{position:absolute;left:19px;top:62px;width:242px;height:24px;background:var(--field);font-size:10px;color:#666;padding:5px 8px}
.news .btn{position:absolute;left:19px;top:95px;width:242px;height:24px;background:var(--orange);font-size:12px;color:#fff;text-align:center;line-height:24px}
.news p{position:absolute;left:23px;top:143px;width:215px;font-size:9px;line-height:1.4}
.truck{left:215px;top:475px;width:280px;height:202px}
.truck h3{position:absolute;left:0;top:16px;width:100%;text-align:center;color:var(--blue);font-style:italic;font-weight:700;font-size:15px}
.truck .pic{position:absolute;left:62px;top:49px;width:160px;height:110px;background:linear-gradient(#c8c8c8,#a8a8a8);border-radius:8px}
.truck .arr{position:absolute;top:92px;width:14px;height:34px;stroke:var(--orange);fill:none;stroke-width:1.5}
.truck p{position:absolute;left:0;top:168px;width:100%;text-align:center;font-size:9.5px;line-height:1.35}
.about{left:505px;top:475px;width:473px;height:202px}
.about h2{position:absolute;left:14px;top:14px}
.about .txt{position:absolute;left:37px;top:54px;width:400px;font-size:9.5px;line-height:1.35}
.about .txt p{margin-bottom:12px}
.partners{left:215px;top:694px;width:763px;height:94px}
.partners h2{position:absolute;left:14px;top:6px}
.logos{position:absolute;left:40px;top:38px;width:700px;display:flex;justify-content:space-between;align-items:center;font-size:17px;font-weight:700;color:#8a8a8a}
.footer{left:229px;top:797px;font-size:8px;color:#555}
.social{left:918px;top:796px;display:flex;gap:9px}
.social i{width:8px;height:8px;border-radius:50%;background:#888;display:inline-block}
</style>
</head>
<body>
<div class="abs topbar">
  <div class="abs follow">Finde uns auf Netzwerk <i></i></div>
  <div class="abs auth">Login&nbsp; I&nbsp;&nbsp; Anmelden</div>
</div>

<div class="abs header"></div>
<div class="abs brand"><i></i>pausenteller</div>

<div class="abs tab">▸ Erweiterete Suche</div>
<form class="abs search">
  <div class="inner">
    <div class="field" style="left:3px;width:152px">Dein aktueller Standort</div>
    <div class="drop" style="left:155px"></div>
    <div class="field" style="left:189px;width:54px">Montag</div>
    <div class="drop" style="left:243px"></div>
    <div class="field" style="left:278px;width:156px">Was schmeckt Ihnen ?</div>
    <div class="drop" style="left:434px"></div>
    <div class="go">Suchen</div>
  </div>
</form>

<nav class="abs nav">
  <span style="left:25px"><svg viewBox="0 0 20 20"><path d="M2 10 10 3l8 7M5 8v9h4v-5h2v5h4V8"/></svg>Home</span>
  <span style="left:125px"><svg viewBox="0 0 20 20"><rect x="3" y="4" width="14" height="11" rx="2"/><path d="M3 9h14M6 17v-2M14 17v-2"/></svg>FoodTrucks</span>
  <span style="left:268px"><svg viewBox="0 0 20 20"><path d="M3 8a7 5 0 0 1 14 0zM3 11h14M3 14h14v2H3z"/></svg>Imbisse</span>
  <span style="left:380px"><svg viewBox="0 0 24 20"><path d="M2 16h20M4 16a8 8 0 0 1 16 0M12 6V4"/></svg>Restaurants</span>
  <span style="left:529px"><svg viewBox="0 0 20 20"><path d="M11 3h6v6l-8 8-6-6z"/><circle cx="14" cy="6" r="1"/></svg>Kosten</span>
  <span style="left:655px"><svg viewBox="0 0 20 20"><circle cx="10" cy="6" r="4"/><path d="M3 18a7 7 0 0 1 14 0z"/></svg>Über Uns</span>
</nav>

<div class="abs photo" role="img" aria-label="Unscharfes Foto eines Mittagstellers mit Fleisch und Gemüse als Hintergrund"></div>

<section class="abs card welcome">
  <h2><svg width="12" height="18" viewBox="0 0 12 18"><path d="M6 0a6 6 0 0 1 6 6c0 4-6 12-6 12S0 10 0 6a6 6 0 0 1 6-6z" fill="#999"/><circle cx="6" cy="6" r="2" fill="#fff"/></svg>Herzlich Willkommen <em>pausenteller</em></h2>
  <p class="lead">Wissen Sie schon was es gleich zum Mittag gibt ?</p>
  <ul><li><i></i>Pizza ?</li><li><i></i>Cheesburger ?</li><li><i></i>Vegearisches ?</li></ul>
  <div class="voices" role="img" aria-label="Gezeichnete Sprechblasen mit typischen Mittagspausen-Sorgen"></div>
  <p class="body"><span class="hl">pausenteller</span> kümmert sich Dich. Von uns erfährst Von Uns erfährst du wo die nächste Location ist die dich satt macht. So gibt es endlich mal Abwechslung in deiner Pause.</p>
</section>

<section class="abs card news">
  <h2><svg width="20" height="14" viewBox="0 0 20 14"><rect width="20" height="14" fill="#999"/><path d="M0 0l10 8 10-8" stroke="#fff" fill="none"/></svg>Newsltter empfangen?</h2>
  <div class="mail">Ihre E-Mailadresse hier eintragen</div>
  <div class="btn">Jetzt bestellen</div>
  <p>Der Newsletter informiert dich über Events rund um das ( mobile) Essen...</p>
</section>

<section class="abs card truck">
  <h3>Grüner Bernd Bürger</h3>
  <svg class="arr" style="left:18px" viewBox="0 0 14 34"><path d="M12 2 2 17l10 15"/></svg>
  <div class="pic" role="img" aria-label="Grafik von Burger und Pommes"></div>
  <svg class="arr" style="left:245px" viewBox="0 0 14 34"><path d="M2 2l10 15L2 32"/></svg>
  <p>„Lecker mit frischen Salat und Hausmannsoße<br>innerhalb von 5 min fertig“</p>
</section>

<section class="abs card about">
  <h2><svg width="14" height="18" viewBox="0 0 14 18"><circle cx="7" cy="5" r="4" fill="#999"/><path d="M0 18a7 8 0 0 1 14 0z" fill="#999"/></svg>Was ist <em>pausenteller?</em></h2>
  <div class="txt">
    <p><span class="hl">pausenteller</span> beherbergt aktuell 9 Food Trucks/Imbisse/Restaurants über ganz Deutschland verteilt. Insgesamt werden von Ihnen an 8 Standorten Speisen aller Art angeboten.</p>
    <p>Insgesamt wurden auf <span class="hl">pausenteller</span> bereits 11 Bewertungen und 0 Events eingetragen.</p>
    <p>Das Special für Food Trucks sind unsere aktuell 1 angebotenen Stellplätze.</p>
    <p>Hier kann man neue lukrative Verkaufspunkte finden und direkt mit dem Anbieter in Kontakt treten.</p>
  </div>
</section>

<section class="abs card partners">
  <h2><svg width="16" height="16" viewBox="0 0 16 16"><path d="M8 0l2.4 5.2 5.6.6-4.2 3.8 1.2 5.6L8 12.4 3 15.2l1.2-5.6L0 5.8l5.6-.6z" fill="#999"/></svg>Unsere Partner</h2>
  <div class="logos"><span>Tafelhaus Nord</span><span>Kochkiste</span><span>Feldmarkt</span><span>Kornwerk</span><span>Brotbund Süd</span></div>
</section>

<div class="abs footer">Impressum&nbsp; I AGB&nbsp; I Kontakt</div>
<div class="abs social"><i></i><i></i><i></i></div>
</body>
</html>
```